Helping Seniors and their families start the discussion about driver safety, and explore options to preserve senior independence.
Target Market(s)
Seniors and their families
Industry/Entity Type
Non Profit
Number of Pages Required
4 page
Font styles to use
Sans Serif
Requirements
Must have
- Logo
- Application for Amber Crossings Registration

Nice to have
- Colorful, and designed for Senior Citizens and their Families

```html
<!DOCTYPE html>
<html lang="en">
<head>
<meta charset="utf-8">
<title>Amber Crossings — Premier Transportation for Seniors</title>
<link href="https://fonts.googleapis.com/css2?family=Lato:wght@400;700;900&display=swap" rel="stylesheet">
<style>
:root{
  --green:#5ac779;
  --green-dark:#0f8a3e;
  --blue:#2a9fd6;
  --ink:#3d4246;
  --muted:#7d8287;
  --soft:#a3a7ab;
  --line:#e9ecef;
  --white:#ffffff;
}
*{box-sizing:border-box;margin:0;padding:0}
html,body{width:1200px;height:1200px;overflow:hidden;background:var(--white)}
body{font-family:"Lato",sans-serif;color:var(--ink);position:relative}
.brand{position:absolute;left:144px;top:36px;display:flex;align-items:center;gap:8px;font-weight:900;font-size:24px;color:var(--green-dark)}
.brand-dot{width:14px;height:14px;border-radius:50%;background:var(--green-dark)}
.nav{position:absolute;top:46px;left:434px;display:flex;gap:39px;font-size:14.5px;color:var(--muted)}
.nav a{color:inherit;text-decoration:none;padding-bottom:4px}
.nav a.active{color:var(--ink);border-bottom:2px solid var(--blue)}
.reserve{position:absolute;right:144px;top:38px;display:flex;align-items:center;gap:8px}
.reserve small{display:block;font-size:12px;color:var(--ink)}
.reserve strong{display:block;font-size:17px;font-weight:400;color:var(--ink)}
.hero{position:absolute;left:144px;top:106px;width:912px;height:336px;background:linear-gradient(100deg,#d5d6d8 0%,#9fb1c0 45%,#5d6b76 75%,#8fa0a6 100%);}
.hero h1{position:absolute;top:114px;width:100%;text-align:center;color:var(--white);font-weight:400;font-size:32px;line-height:39px;letter-spacing:.3px}
.btn{display:inline-block;background:var(--green);color:var(--white);font-weight:900;letter-spacing:1.6px;font-size:12px;text-align:center;text-decoration:none}
.hero .btn{position:absolute;left:293px;top:206px;width:328px;height:41px;line-height:41px}
.dots{position:absolute;top:306px;left:0;width:100%;display:flex;justify-content:center;gap:5px}
.dots span{width:6px;height:6px;border-radius:50%;background:rgba(255,255,255,.45)}
.dots span:first-child{background:var(--white)}
.intro{position:absolute;top:484px;width:1200px;text-align:center}
.intro h2{font-size:26px;font-weight:400;color:var(--ink)}
.intro p{margin-top:10px;font-size:17.5px;color:var(--soft)}
.card{position:absolute;padding:18px 20px;background:var(--white);box-shadow:0 1px 6px rgba(0,0,0,.08);font-size:12.3px;line-height:17.6px;color:var(--muted)}
.card h3{font-size:18px;font-weight:400;color:var(--ink);margin-bottom:8px;display:flex;align-items:center;gap:10px}
.card.green{background:var(--green);color:var(--white)}
.card.blue{background:var(--blue);color:var(--white)}
.card.green h3,.card.blue h3{color:var(--white)}
.cta{position:absolute;left:506px;top:1090px;width:188px;height:40px;line-height:40px;border-radius:20px}
</style>
</head>
<body>
<header>
  <div class="brand"><span class="brand-dot"></span>Amber Crossings</div>
  <nav class="nav">
    <a class="active" href="#">Home</a><a href="#">Services</a><a href="#">Application</a><a href="#">Contact</a>
  </nav>
  <div class="reserve">
    <svg width="26" height="26" viewBox="0 0 26 26" fill="none" stroke="#2a9fd6" stroke-width="1.6" stroke-linecap="round"><path d="M12 3 L9 5 C10 11 14 17 19 20 L22 18 L18 14 L16 15 C14 13 13 11 12 9 L13 7 Z"/><path d="M2 22h1M5 22h1M8 22h1"/></svg>
    <div><small>Reservation line</small><strong>555-014-2780</strong></div>
  </div>
</header>

<section class="hero" role="img" aria-label="Smiling senior man being helped into a car by caregivers">
  <h1>Premier Transportation for Seniors<br>and Disabled Persons</h1>
  <a class="btn" href="#">GO WHEN AND WHERE YOU WANT TO GO</a>
  <div class="dots"><span></span><span></span><span></span></div>
</section>

<section class="intro">
  <h2>Be independent</h2>
  <p>Empowering Seniors with Independence and Caregivers with Peace of Mind</p>
</section>

<article class="card green" style="left:144px;top:581px;width:444px;height:150px">
  <h3>Convenience</h3>
  <p>With Amber Crossings, you can schedule transportation at a time that is convenient for you, eliminating the need to work around the schedule of family and friends. Transportation is not limited to medical appointments. You can travel to the mall, concerts, church, grocery store, theater, etc. Go when and where you want to go!</p>
</article>

<article class="card" style="left:610px;top:581px;width:446px;height:117px">
  <h3>Specialized Services
    <svg width="20" height="20" viewBox="0 0 20 20" fill="none" stroke="#5ac779" stroke-width="1.3"><circle cx="10" cy="10" r="3"/><path d="M10 1.5v3M10 15.5v3M1.5 10h3M15.5 10h3M4 4l2.1 2.1M13.9 13.9L16 16M4 16l2.1-2.1M13.9 6.1L16 4"/><circle cx="10" cy="10" r="6"/></svg>
  </h3>
  <p>Our team is experienced in providing services to seniors and individuals with physical and cognitive issues such as blindness, cancer, hip/knee replacement, Autism, Alzheimer's, loss of hearing, OM, etc.</p>
</article>

<article class="card blue" style="left:612px;top:722px;width:444px;height:116px">
  <h3>Safety</h3>
  <p>Your safety is our first priority. We follow you from location to location, and then follow up with you to see how the ride was and if you have questions or concerns.</p>
</article>

<article class="card" style="left:144px;top:756px;width:444px;height:153px">
  <h3>Understanding Your Needs
    <svg width="22" height="20" viewBox="0 0 22 20" fill="none" stroke="#5ac779" stroke-width="1.3"><path d="M3 15 L2 19 L6 16 A8 7 0 1 0 3 15Z"/><circle cx="7" cy="9" r=".6"/><circle cx="10" cy="9" r=".6"/><circle cx="13" cy="9" r=".6"/></svg>
  </h3>
  <p>We understand that everyone is not alike, therefore, needs are not alike. It is important to us that our services meet your needs. Before scheduling service, we may suggest a free one-on-one consultation with you and/or your caregiver. We will listen and pay strict attention to your instructions and tailor our services to meet your needs.</p>
</article>

<article class="card" style="left:612px;top:862px;width:444px;height:152px">
  <h3>Evening and Weekend Service
    <svg width="22" height="22" viewBox="0 0 22 22" fill="none" stroke="#5ac779" stroke-width="1.3" stroke-linecap="round"><circle cx="11" cy="11" r="4.5"/><path d="M11 1v2.5M11 18.5V21M1 11h2.5M18.5 11H21M4 4l1.8 1.8M16.2 16.2L18 18M4 18l1.8-1.8M16.2 5.8L18 4"/></svg>
  </h3>
  <p>We do not stop at 6 pm each weekday. We encourage our clients to remain sociably active, and understand that most family and community life occur in evening and on weekends. To support our clients, we offer services 7 days a week, early morning and late nights are available by request and availability.</p>
</article>

<article class="card" style="left:144px;top:934px;width:444px;height:115px">
  <h3>Affordable Rates
    <svg width="21" height="21" viewBox="0 0 21 21" fill="none" stroke="#5ac779" stroke-width="1.3"><circle cx="10.5" cy="10.5" r="9.5"/><path d="M6.5 10.5l3 3 5-6"/></svg>
  </h3>
  <p>Our rates are less than rates of most taxi and transportation companies in the Metro Riverside Area and beyond. We can estimate a rate for you, allowing clients and caregivers to budget expenses.</p>
</article>

<a class="btn cta" href="#">I WANT A SAFE RIDE</a>
</body>
</html>
```